PowerPoint Design Project

Have a Power Point we want someone to make really cool! About 10 pages and just need someone to build on what we've done.

Target Market(s)

Technology Mfgs/VARs Sales People and VP of Sales

Industry/Entity Type

Build

```html
<!DOCTYPE html>
<html lang="en">
<head>
<meta charset="utf-8">
<title>Harbor Line Capital – Sales Deck</title>
<link href="https://fonts.googleapis.com/css2?family=Arimo:ital,wght@0,400;0,700;1,700&display=swap" rel="stylesheet">
<style>
:root{
  --stage:#ece9e4;
  --paper:#ffffff;
  --brand-blue:#1f5aa6;
  --bar-blue:#1d4f8f;
  --brand-green:#5f8f2a;
  --ink:#3c3c3c;
  --muted:#8a8a8a;
  --rule:#d6d6d6;
  --badge:#c9ccd1;
}
*{box-sizing:border-box;margin:0;padding:0}
html,body{width:1200px;height:386px;overflow:hidden;background:var(--stage)}
body{position:relative;font-family:"Arimo",Arial,sans-serif;color:var(--ink)}
.slide{position:absolute;width:205px;height:154px;background:var(--paper);overflow:hidden;box-shadow:0 1px 3px rgba(0,0,0,.18)}
.c1{left:19px}.c2{left:250px}.c3{left:482px}.c4{left:713px}.c5{left:946px}
.r1{top:19px}.r2{top:212px}
.slide-footer{position:absolute;left:0;bottom:0;width:100%;height:11px;background:var(--bar-blue);display:flex;align-items:center;justify-content:center;gap:4px;color:#fff;font-size:4.6px;font-weight:700}
.slide-footer::before{content:"";position:absolute;left:0;top:-2px;width:100%;height:2px;background:var(--brand-green)}
.footer-mark{position:absolute;left:3px;top:2px;width:7px;height:7px;background:var(--paper)}
.slide-title{position:absolute;left:10px;top:8px;font-size:8.4px;font-weight:700;color:var(--brand-blue);white-space:nowrap}
.slide-sub{position:absolute;left:10px;top:18px;font-size:6.6px;font-weight:700;color:var(--brand-green)}
.body{font-size:4.2px;line-height:1.35}
.body h4{font-size:4.4px;color:var(--brand-blue);font-weight:700}
.abs{position:absolute}
.placeholder{position:absolute}
/* brand name */
.brand{position:absolute;left:0;width:100%;display:flex;align-items:center;justify-content:center;gap:5px}
.brand-mark{width:14px;height:14px;background:var(--brand-green)}
.brand-name{font-size:11px;font-weight:700;color:var(--brand-blue);line-height:1;white-space:nowrap}
.cover-head{position:absolute;left:0;width:100%;text-align:center;font-size:9px;font-weight:700;color:var(--brand-blue);line-height:1.3}
/* offer grid */
.offer{display:grid;grid-template-columns:1fr 1fr;gap:6px 10px;left:10px;top:32px;width:186px}
/* about */
.goal{left:0;width:100%;text-align:center;color:var(--brand-blue);font-weight:700}
/* partners */
.badges{left:10px;top:26px;width:186px;display:grid;grid-template-columns:repeat(3,1fr);gap:7px 8px}
.badge{height:11px;background:var(--badge);border-radius:2px}
/* bullets */
.facts{left:112px;top:48px;width:86px;list-style:none}
.facts li{display:flex;gap:3px;margin-bottom:6px}
.facts li::before{content:"";flex:none;width:4px;height:4px;border-radius:50%;background:var(--brand-blue);margin-top:.5px}
.tagline{left:0;width:100%;text-align:center;font-size:5.6px;font-weight:700;font-style:italic;color:var(--brand-green)}
.roi-label{font-size:5.6px;font-weight:700;color:var(--brand-blue);line-height:1.2}
.lease h4{margin-top:4px}
.thanks{left:0;width:100%;text-align:center}
</style>
</head>
<body>

<!-- Cover -->
<section class="slide c1 r1">
  <div class="brand" style="top:42px">
    <span class="brand-mark"></span>
    <span class="brand-name">Harbor Line Capital</span>
  </div>
  <h1 class="cover-head" style="top:84px">Make Financing<br>Part of Your Sales Cycle</h1>
  <footer class="slide-footer"><span class="footer-mark"></span>555.210.4400 <span>|</span> www.HarborLineCapital.com</footer>
</section>

<!-- Why offer financing -->
<section class="slide c2 r1">
  <h2 class="slide-title">Why Offer Financing…</h2>
  <p class="slide-sub">How will this help you make money?</p>
  <div class="abs offer body">
    <div><h4>Increased Sales</h4>15-25% of all IT Equipment &amp; Software is leased or financed</div>
    <div><h4>Fast Quotes &amp; Pre-Approval</h4>Start-Ups, Growth Stage, VCs &amp; Fortune 500 Corporations</div>
    <div><h4>Increased Margins</h4>Focus on Monthly Payments vs. Total Cost. Clients likely to lease additional equipment</div>
    <div><h4>Sell More Often</h4>Make it easier for your customers to acquire new equipment, upgrade current equipment, or add on to existing equipment</div>
    <div><h4>Prospecting &amp; Closing Tools</h4>Example (6 Month Deferred)</div>
    <div><h4>Extra Set of Eyes and Ears</h4>Speak with the CFO or Controller early in the sales cycle</div>
  </div>
  <footer class="slide-footer"><span class="footer-mark"></span>555.210.4400 <span>|</span> www.HarborLineCapital.com</footer>
</section>

<!-- About us -->
<section class="slide c3 r1">
  <h2 class="slide-title">About Us</h2>
  <div class="abs body" style="left:10px;top:28px;width:98px">
    <p>Leading Technology Financing and Leasing Company founded in 2003</p><br>
    <p>Direct Lender and syndication lines with national large network of banks and funding partners</p><br>
    <p>Specialize in IT – WE GET IT</p><br>
    <p>Partner Focused: We consider you our primary customer</p><br>
    <p>Sales Driven: We push as hard as you do to close… not order takers!</p>
  </div>
  <div class="placeholder" role="img" aria-label="Photo of an ocean pier at sunset" style="left:112px;top:19px;width:86px;height:68px;background:linear-gradient(180deg,#8fb3cf 0%,#c9c3b4 55%,#4d6f8a 100%)"></div>
  <p class="abs goal" style="top:111px;font-size:6.6px">Goal</p>
  <p class="abs goal" style="top:120px;font-size:5.4px;font-style:italic;color:var(--brand-green)">Help our Vendor-Partners accelerate their bottom line</p>
  <footer class="slide-footer"><span class="footer-mark"></span>555.210.4400 <span>|</span> www.HarborLineCapital.com</footer>
</section>

<!-- Partners -->
<section class="slide c4 r1">
  <h2 class="slide-title">Who We Partner with…</h2>
  <div class="abs badges" aria-label="Partner badges">
    <span class="badge" style="width:60%"></span><span class="badge" style="width:70%"></span><span class="badge"></span>
    <span class="badge" style="width:40%"></span><span class="badge" style="width:75%"></span><span class="badge" style="width:85%"></span>
    <span class="badge" style="width:40%"></span><span class="badge" style="width:55%"></span><span class="badge" style="width:90%"></span>
    <span class="badge" style="width:65%"></span><span class="badge" style="width:60%"></span><span class="badge" style="width:95%"></span>
    <span class="badge" style="width:75%"></span><span class="badge" style="width:85%"></span><span class="badge" style="width:80%"></span>
    <span class="badge"></span><span class="badge" style="width:30%"></span><span class="badge" style="width:95%"></span>
  </div>
  <footer class="slide-footer"><span class="footer-mark"></span>555.210.4400 <span>|</span> www.HarborLineCapital.com</footer>
</section>

<!-- Leasing industry -->
<section class="slide c5 r1">
  <h2 class="slide-title">The Leasing Industry Today</h2>
  <div class="placeholder" role="img" aria-label="Illustration of a rising orange arrow over a bar chart" style="left:12px;top:42px;width:86px;height:72px;background:linear-gradient(135deg,#dfe7e0 0%,#f0b25a 60%,#e7893a 100%)"></div>
  <ul class="abs facts body">
    <li>Technology Financing is estimated to be over a $92 billion industry</li>
    <li>80% of all businesses lease</li>
    <li>2013 Hardware &amp; Software sales growth estimate up to 4.9%</li>
    <li>43% of small businesses need funding sources</li>
  </ul>
  <footer class="slide-footer"><span class="footer-mark"></span>555.210.4400 <span>|</span> www.HarborLineCapital.com</footer>
</section>

<!-- ROI -->
<section class="slide c1 r2">
  <h2 class="slide-title">Which ROI would your client prefer?</h2>
  <svg class="abs" style="left:8px;top:26px" width="104" height="40" viewBox="0 0 104 40" aria-label="Cash ROI line chart">
    <rect width="104" height="40" fill="#f1f1f1"/>
    <line x1="4" y1="20" x2="100" y2="20" stroke="#bbb" stroke-width=".4"/>
    <rect x="10" y="14" width="2" height="6" fill="#c33"/><rect x="14" y="14" width="2" height="6" fill="#c33"/>
    <polyline points="8,22 20,21 32,20 44,19 56,18 68,17 80,15 96,8" fill="none" stroke="#c55" stroke-width=".8"/>
    <rect x="86" y="2" width="12" height="4" fill="var(--brand-green)"/>
  </svg>
  <p class="abs roi-label" style="left:122px;top:42px">Cash or<br>Net terms ROI</p>
  <p class="abs roi-label" style="left:56px;top:95px;text-align:right">Financing or<br>Leasing ROI</p>
  <svg class="abs" style="left:96px;top:82px" width="104" height="38" viewBox="0 0 104 38" aria-label="Leasing ROI line chart">
    <rect width="104" height="38" fill="#f1f1f1"/>
    <line x1="4" y1="22" x2="100" y2="22" stroke="#bbb" stroke-width=".4"/>
    <g fill="#c55"><rect x="20" y="17" width="2" height="5"/><rect x="28" y="17" width="2" height="5"/><rect x="36" y="17" width="2" height="5"/><rect x="44" y="17" width="2" height="5"/><rect x="52" y="17" width="2" height="5"/><rect x="60" y="17" width="2" height="5"/></g>
    <polyline points="8,22 30,21 50,19 70,16 96,12" fill="none" stroke="#c55" stroke-width=".8"/>
    <rect x="86" y="2" width="12" height="4" fill="var(--brand-green)"/>
  </svg>
  <p class="abs tagline" style="top:127px">Same project, Same benefits, Quicker payback!</p>
  <footer class="slide-footer"><span class="footer-mark"></span>555.210.4400 <span>|</span> www.HarborLineCapital.com</footer>
</section>

<!-- Why lease -->
<section class="slide c2 r2">
  <h2 class="slide-title">Why your clients decide to lease</h2>
  <div class="abs body lease" style="left:10px;top:22px;width:100px">
    <h4>Cash Flow</h4>
    <p>• $75,000 vs. $1,995 / month<br>• $150,000 vs. $3,050 / month<br>• $500,000 vs. $9,895 / month</p>
    <h4>Tax Advantages</h4>
    <p>• Advantages of OpEx vs. CapEx<br>• Section 179 100% Deductions</p>
    <h4>Simplicity</h4>
    <p>• 1 page applications for $10K to $250K</p>
    <h4>Flexibility</h4>
    <p>• Term (24, 36, 48, 60 months)<br>• Deferred Payments<br>• Offer 0%</p>
  </div>
  <div class="placeholder" role="img" aria-label="Photo of a pile of banknotes" style="left:102px;top:44px;width:96px;height:56px;border-radius:40% 40% 10% 10%;background:radial-gradient(ellipse at 50% 60%,#9aa58a 0%,#6f7d66 60%,#e9ebe6 100%)"></div>
  <footer class="slide-footer"><span class="footer-mark"></span>555.210.4400 <span>|</span> www.HarborLineCapital.com</footer>
</section>

<!-- Calculator -->
<section class="slide c3 r2">
  <h2 class="slide-title">Harbor Line Capital's Cloud Calculator</h2>
  <svg class="abs" style="left:58px;top:22px" width="90" height="116" viewBox="0 0 90 116" aria-label="Calculator form">
    <rect width="90" height="116" fill="#fff" stroke="var(--rule)" stroke-width=".5"/>
    <rect x="4" y="4" width="6" height="6" fill="var(--brand-green)"/>
    <rect x="12" y="5" width="22" height="3" fill="var(--brand-blue)"/>
    <g fill="#ddd"><rect x="4" y="16" width="82" height="1.2"/><rect x="4" y="19" width="70" height="1.2"/></g>
    <g fill="none" stroke="#aaa" stroke-width=".4"><rect x="4" y="26" width="38" height="4"/><rect x="48" y="26" width="38" height="4"/><rect x="4" y="33" width="38" height="4"/><rect x="48" y="33" width="38" height="4"/><rect x="4" y="40" width="38" height="4"/></g>
    <rect x="4" y="52" width="82" height="5" fill="var(--brand-green)"/>
    <rect x="4" y="60" width="82" height="3" fill="#cfe0b9"/>
    <g fill="none" stroke="#bbb" stroke-width=".4"><rect x="4" y="66" width="82" height="14"/><rect x="4" y="86" width="82" height="14"/></g>
    <g fill="#e06060"><rect x="66" y="70" width="6" height="4"/><rect x="66" y="90" width="6" height="4"/></g>
    <rect x="4" y="104" width="82" height="3" fill="var(--brand-green)"/>
  </svg>
  <footer class="slide-footer"><span class="footer-mark"></span>555.210.4400 <span>|</span> www.HarborLineCapital.com</footer>
</section>

<!-- Proposal -->
<section class="slide c4 r2">
  <h2 class="slide-title">Proposal from the Cloud Calculator</h2>
  <svg class="abs" style="left:56px;top:21px" width="96" height="118" viewBox="0 0 96 118" aria-label="Proposal letter">
    <rect width="96" height="118" fill="#fff" stroke="var(--rule)" stroke-width=".5"/>
    <rect x="6" y="5" width="6" height="6" fill="var(--brand-green)"/>
    <rect x="60" y="5" width="28" height="1.2" fill="#999"/><rect x="60" y="8" width="22" height="1.2" fill="#999"/>
    <rect x="70" y="14" width="20" height="3" fill="#e06060"/>
    <g fill="#bbb"><rect x="6" y="20" width="20" height="1"/><rect x="6" y="23" width="24" height="1"/><rect x="6" y="26" width="18" height="1"/></g>
    <g fill="#ccc"><rect x="6" y="34" width="84" height="1"/><rect x="6" y="37" width="80" height="1"/><rect x="6" y="40" width="84" height="1"/></g>
    <g fill="none" stroke="#999" stroke-width=".4"><rect x="6" y="46" width="84" height="14"/><line x1="6" y1="50" x2="90" y2="50"/><line x1="6" y1="55" x2="90" y2="55"/></g>
    <g fill="#ccc"><rect x="6" y="66" width="84" height="1"/><rect x="6" y="69" width="76" height="1"/><rect x="6" y="72" width="84" height="1"/><rect x="6" y="75" width="60" height="1"/><rect x="6" y="82" width="84" height="1"/><rect x="6" y="85" width="70" height="1"/><rect x="6" y="94" width="20" height="1"/><rect x="6" y="100" width="24" height="1"/><rect x="20" y="112" width="56" height="1"/></g>
  </svg>
  <footer class="slide-footer"><span class="footer-mark"></span>555.210.4400 <span>|</span> www.HarborLineCapital.com</footer>
</section>

<!-- Thank you -->
<section class="slide c5 r2">
  <div class="brand" style="top:24px">
    <span class="brand-mark"></span>
    <span class="brand-name">Harbor Line Capital</span>
  </div>
  <p class="abs thanks" style="top:64px;font-size:9.4px;font-weight:700;color:var(--brand-green)">THANK YOU</p>
  <p class="abs thanks" style="top:84px;font-size:5.6px;line-height:1.5;color:var(--brand-blue)">480 Ocean Avenue, Suite 210<br>Seal Point, CA 90000</p>
  <p class="abs thanks" style="top:106px;font-size:7px;font-weight:700;color:var(--brand-blue)">Fax: 555.210.4401</p>
  <footer class="slide-footer"><span class="footer-mark"></span>555.210.4400 <span>|</span> www.HarborLineCapital.com</footer>
</section>

</body>
</html>
```